Varnell Skyworks Limited

Started a consulting business 12 months ago and have since moved location and have grown and seek to identify my self to the industry.
Specializing in quality solutions, business documentation and maintenance solution's

Industry/Entity Type

Business

```html
<!DOCTYPE html>
<html lang="en">
<head>
<meta charset="utf-8">
<title>Varnell Skyworks Limited – Business Card</title>
<link rel="stylesheet" href="https://fonts.googleapis.com/css2?family=Exo+2:wght@400;500&family=Arimo:wght@400&display=swap">
<style>
  :root {
    --backdrop: #8e8e8e;
    --card-dark: #3a3a3a;
    --card-light: #f4f4f4;
    --card-light-edge: #dcdcdc;
    --ink: #333333;
    --rule: #3a3a3a;
    --stripe: #d6d6d6;
  }
  * { margin: 0; padding: 0; box-sizing: border-box; }
  html, body {
    width: 1200px; height: 894px; overflow: hidden;
    background: var(--backdrop);
  }
  .canvas { position: relative; width: 1200px; height: 894px; }
  .card {
    position: absolute; left: 250px; width: 700px; height: 400px;
    overflow: hidden;
  }
  /* Back of card */
  .card-back { top: 27px; background: var(--card-dark); }
  .brand-pill {
    position: absolute; left: 290px; right: 0; top: 186px; height: 100px;
    background: linear-gradient(180deg, #ffffff, #e6e6e6);
    border-radius: 50px 0 0 50px;
    display: flex; align-items: center; padding-left: 36px;
  }
  .brand-name {
    font-family: "Arimo", Arial, sans-serif; font-size: 30px; font-weight: 400;
    color: var(--card-dark); white-space: nowrap;
  }
  .brand-stripe {
    position: absolute; left: 540px; right: 0; top: 298px; height: 16px;
    background: var(--stripe);
  }
  /* Front of card */
  .card-front {
    top: 467px;
    background: linear-gradient(160deg, var(--card-light) 0%, #ffffff 45%, var(--card-light-edge) 100%);
    font-family: "Exo 2", sans-serif; color: var(--ink);
  }
  .holder-name {
    position: absolute; left: 44px; top: 34px;
    font-size: 26px; font-weight: 500; letter-spacing: 0.5px;
  }
  .holder-title {
    position: absolute; left: 46px; top: 68px;
    font-size: 11px; letter-spacing: 0.8px;
  }
  .contact-list {
    position: absolute; left: 46px; top: 96px; list-style: none;
    font-size: 17px; line-height: 25px;
  }
  .contact-list li { display: flex; }
  .contact-label { width: 86px; }
  .contact-list .contact-web .contact-label { width: auto; margin-right: 6px; }
  .rule { position: absolute; height: 2px; background: var(--rule); }
  .rule-contacts { left: 40px; width: 420px; top: 202px; }
  .address {
    position: absolute; left: 44px; top: 214px;
    display: flex; align-items: center; gap: 10px;
    font-size: 17px; letter-spacing: 0.5px; white-space: nowrap;
  }
  .address svg { width: 14px; height: 20px; }
  .rule-address { left: 40px; right: 0; top: 250px; }
  .rule-base-1 { left: 0; right: 0; top: 318px; }
  .rule-base-2 { left: 0; right: 0; top: 344px; }
  .front-pill {
    position: absolute; left: 540px; right: 0; top: 110px; height: 120px;
    background: var(--card-dark);
    border-radius: 60px 0 0 60px;
  }
</style>
</head>
<body>
<main class="canvas">
  <section class="card card-back" aria-label="Card back">
    <div class="brand-pill"><span class="brand-name">Varnell Skyworks Limited</span></div>
    <div class="brand-stripe"></div>
  </section>

  <section class="card card-front" aria-label="Card front">
    <h1 class="holder-name">Daniel Hargrove</h1>
    <p class="holder-title">GENERAL MANAGER</p>
    <ul class="contact-list">
      <li><span class="contact-label">Phone:</span><span>012 555 0147</span></li>
      <li><span class="contact-label">Fax:</span><span>012 555 0148</span></li>
      <li><span class="contact-label">Email:</span><span>hello@varnellsky.com</span></li>
      <li class="contact-web"><span class="contact-label">website:</span><span>www.varnellskyworks.com</span></li>
    </ul>
    <div class="rule rule-contacts"></div>
    <p class="address">
      <svg viewBox="0 0 14 20" aria-hidden="true"><path d="M7 0C3.1 0 0 3.1 0 7c0 5 7 13 7 13s7-8 7-13c0-3.9-3.1-7-7-7zm0 9.6A2.6 2.6 0 1 1 7 4.4a2.6 2.6 0 0 1 0 5.2z" fill="#333"/></svg>
      <span>041,9th floor,Harbor Crest Road Norbury</span>
    </p>
    <div class="rule rule-address"></div>
    <div class="rule rule-base-1"></div>
    <div class="rule rule-base-2"></div>
    <div class="front-pill"></div>
  </section>
</main>
</body>
</html>
```